Bay Bolts

I am starting a sharpening service for knives, scissors, and garden tools. It's a sole proprietorship, so it's a small business. The business name is "Bay Bolt." A one or two-page website is fine. Mark Orchard has created a logo for me. There should be pictures of the things I sharpen. There will also be a price list for sharpened items. My address is: 18302 Pellman Way, Stevenson Ranch, CA 91381. Phone number is 661-555-0173

```html
<!DOCTYPE html>
<html lang="en">
<head>
<meta charset="utf-8">
<title>Bay Bolts — Sharpening Service</title>
<link rel="stylesheet" href="https://fonts.googleapis.com/css2?family=Montserrat:wght@500;600;700;800&family=Poppins:wght@400;500;600&display=swap">
<style>
  :root {
    --ink: #111111;
    --white: #ffffff;
    --paper-grey: #f1f1f1;
    --footer-bg: #121212;
    --field-border: #555555;
    --muted: #cfcfcf;
    --hero-dark: #1f2a28;
    --hero-mid: #33403c;
  }
  * { box-sizing: border-box; margin: 0; padding: 0; }
  html, body { width: 1200px; height: 4662px; overflow: hidden; }
  body { position: relative; background: var(--white); color: var(--ink); font-family: "Poppins", sans-serif; }
  .abs { position: absolute; }
  .heading { font-family: "Montserrat", sans-serif; font-weight: 800; text-transform: uppercase; letter-spacing: 0.5px; }

  /* header */
  .site-header { left: 0; top: 0; width: 1200px; height: 85px; background: var(--white); }
  .brand { left: 121px; top: 24px; font-family: "Poppins", sans-serif; font-weight: 500; font-size: 30px; color: #333; }
  .nav { top: 34px; font-family: "Montserrat", sans-serif; font-weight: 500; font-size: 14px; color: #222; }
  .header-call { left: 914px; top: 34px; font-family: "Montserrat", sans-serif; font-weight: 500; font-size: 14px; display: flex; align-items: center; gap: 8px; }

  /* hero */
  .hero { left: 0; top: 85px; width: 1200px; height: 597px;
    background: radial-gradient(ellipse at 25% 45%, #5d5a55 0%, var(--hero-mid) 35%, var(--hero-dark) 75%); }
  .hero-title { left: 668px; top: 262px; font-size: 62px; color: var(--white); }
  .hero-sub { left: 668px; top: 356px; font-family: "Montserrat", sans-serif; font-weight: 600; font-size: 23px; line-height: 31px; color: var(--white); }
  .hero-rule { left: 668px; top: 440px; width: 412px; height: 1px; background: rgba(255,255,255,0.35); }
  .hero-call { left: 668px; top: 459px; font-family: "Montserrat", sans-serif; font-weight: 600; font-size: 31px; color: var(--white); }

  /* category cards */
  .category-card { top: 787px; height: 288px; border-radius: 14px; display: flex; align-items: center; justify-content: center; text-align: center; }
  .category-card span { font-family: "Montserrat", sans-serif; font-weight: 800; font-size: 48px; line-height: 56px; color: var(--white); text-transform: uppercase; text-shadow: 0 2px 6px rgba(0,0,0,0.45); }
  .card-knives { left: 63px; width: 344px; background: linear-gradient(135deg, #2b2b2d, #5a4330 55%, #222); }
  .card-scissors { left: 431px; width: 344px; background: linear-gradient(135deg, #8c6547, #c0a080 55%, #7b5b41); }
  .card-garden { left: 793px; width: 344px; background: linear-gradient(135deg, #4c7a2c, #2f5a1d 60%, #6b9a3a); }

  /* about */
  .about { left: 0; top: 1178px; width: 1200px; height: 581px; background: var(--paper-grey); }
  .about-title { left: 119px; top: 1276px; font-size: 42px; line-height: 46px; }
  .stroke { height: 6px; border-radius: 3px; background: var(--ink); }
  .about-text, .service-text { font-size: 14px; line-height: 24px; color: #222; }
  .about-text { left: 119px; top: 1419px; width: 400px; }
  .about-photo { left: 561px; top: 1285px; width: 519px; height: 367px; border-radius: 10px;
    background: linear-gradient(120deg, #d9d6d0, #6f6a62 45%, #b49a86 75%, #3f3a35); }

  /* services */
  .services-title { left: 0; width: 1200px; top: 1853px; text-align: center; font-size: 42px; }
  .service-photo { width: 566px; height: 347px; border-radius: 12px; }
  .photo-knives { left: 87px; top: 1993px; background: linear-gradient(135deg, #3a3a3a, #1c1c1c 60%, #4a4a4a); }
  .photo-scissors { left: 554px; top: 2407px; width: 564px; height: 348px; background: linear-gradient(135deg, #2b3548, #1d2637 60%, #3a465d); }
  .photo-garden { left: 87px; top: 2820px; height: 347px; background: linear-gradient(135deg, #6a5443, #4a3a2e 50%, #7fa24a); }
  .service-name { font-size: 38px; }
  .service-text { width: 360px; }
  .read-more { width: 135px; height: 42px; border: 1.5px solid #333; border-radius: 21px; display: flex; align-items: center; justify-content: center; font-weight: 500; font-size: 14px; background: var(--white); }

  /* banner */
  .quality-banner { left: 0; top: 3298px; width: 1200px; height: 434px;
    background: radial-gradient(ellipse at 60% 45%, #5b5650 0%, #3d3934 45%, #2a2622 100%);
    display: flex; align-items: center; justify-content: center; }
  .quality-banner span { font-family: "Montserrat", sans-serif; font-weight: 800; font-size: 41px; color: var(--white); text-transform: uppercase; letter-spacing: 0.5px; }

  /* social */
  .social-handle { left: 0; width: 1200px; top: 3838px; text-align: center; font-size: 40px; }
  .social-tile { top: 3924px; width: 227px; height: 275px; border-radius: 10px; }
  .tile-1 { left: 119px; background: linear-gradient(135deg, #7b5a3c, #3a2a1e); }
  .tile-2 { left: 364px; background: linear-gradient(135deg, #4a4440, #2c2826); }
  .tile-3 { left: 608px; background: linear-gradient(135deg, #d8d8d4, #6a4a34 60%, #3a3a3a); }
  .tile-4 { left: 853px; background: linear-gradient(135deg, #b9c48a, #6f8a3a 55%, #c23a20); }

  /* footer */
  .site-footer { left: 0; top: 4300px; width: 1200px; height: 362px; background: var(--footer-bg); color: var(--white); }
  .footer-heading { top: 4362px; font-family: "Montserrat", sans-serif; font-weight: 700; font-size: 20px; color: var(--white); }
  .footer-line { left: 154px; font-size: 17px; line-height: 21px; color: var(--white); }
  .field { border: 1px solid var(--field-border); border-radius: 2px; font-size: 11px; color: var(--white); padding: 8px 9px; }
  .submit { left: 947px; top: 4549px; width: 112px; height: 36px; border-radius: 18px; background: var(--white); color: var(--ink); font-family: "Montserrat", sans-serif; font-weight: 700; font-size: 14px; display: flex; align-items: center; justify-content: center; }
  .copyright { left: 0; width: 1200px; top: 4612px; text-align: center; font-size: 14px; color: var(--white); }
</style>
</head>
<body>

<header class="abs site-header">
  <div class="abs brand">Bay Bolts</div>
  <nav>
    <div class="abs nav" style="left:395px">HOME</div>
    <div class="abs nav" style="left:492px">PRICING</div>
    <div class="abs nav" style="left:606px">ABOUT US</div>
    <div class="abs nav" style="left:733px">CONTACT</div>
  </nav>
  <div class="abs header-call">
    <svg width="14" height="14" viewBox="0 0 24 24" aria-hidden="true"><path d="M6.6 10.8a15 15 0 0 0 6.6 6.6l2.2-2.2a1 1 0 0 1 1-.25 11.4 11.4 0 0 0 3.6.57 1 1 0 0 1 1 1V20a1 1 0 0 1-1 1A17 17 0 0 1 3 4a1 1 0 0 1 1-1h3.5a1 1 0 0 1 1 1c0 1.25.2 2.45.57 3.57a1 1 0 0 1-.25 1z" fill="#111"/></svg>
    CALL: 661-555-0173
  </div>
</header>

<section class="abs hero" role="img" aria-label="Row of chef's knives with copper-toned blades on a dark slate surface"></section>
<h1 class="abs heading hero-title">Bay Bolts</h1>
<p class="abs hero-sub">SHARPENING SERVICE FOR KNIVES,<br>SCISSORS, AND GARDEN TOOLS</p>
<div class="abs hero-rule"></div>
<p class="abs hero-call">CALL 661-555-0173</p>

<div class="abs category-card card-knives" role="img" aria-label="Knives with wooden handles laid out on a dark stone board"><span>Knives</span></div>
<div class="abs category-card card-scissors" role="img" aria-label="Pairs of scissors on a wooden table"><span>Scissors</span></div>
<div class="abs category-card card-garden" role="img" aria-label="Gloved hands trimming a hedge with garden shears"><span>Garden<br>Tools</span></div>

<section class="abs about"></section>
<h2 class="abs heading about-title">About<br>Bay Bolts</h2>
<div class="abs stroke" style="left:123px;top:1389px;width:132px"></div>
<p class="abs about-text">Sed ut perspiciatis unde omnis iste natus error sit voluptatem accusantium doloremque laudantium, totam rem aperiam, eaque ipsa quae ab illo inventore veritatis et quasi architecto beatae vitae dicta sunt explicabo. Nemo enim ipsam voluptatem quia voluptas sit aspernatur aut odit aut fugit, sed quia consequuntur magni dolores eos qui ratione voluptatem sequi nesciunt. Neque porro quisquam est, qui dolorem ipsum quia dolor sit amet, consectetur, adipisci</p>
<div class="abs about-photo" role="img" aria-label="Hands sharpening a blade on a grinding wheel with sparks"></div>

<h2 class="abs heading services-title">Our Sharpening Services</h2>
<div class="abs stroke" style="left:536px;top:1923px;width:130px"></div>

<div class="abs service-photo photo-knives" role="img" aria-label="Five kitchen knives with black handles on dark slate"></div>
<h3 class="abs heading service-name" style="left:715px;top:2046px">Knives</h3>
<p class="abs service-text" style="left:715px;top:2109px">Sed ut perspiciatis unde omnis iste natus errorsit voluptatem accusantium doloremque laudantium, totam rem aperiam, eaque ipsa quae ab illo inventore veritatis et quasi archit ecto beatae vitae dicta sulicabo.</p>
<div class="abs read-more" style="left:718px;top:2250px">Read More</div>

<h3 class="abs heading service-name" style="left:119px;top:2460px">Scissors</h3>
<p class="abs service-text" style="left:119px;top:2523px">Sed ut perspiciatis unde omnis iste natus error sit voluptatem accusantium doloremque laudantium, totam rem aperiam, eaque ipsa quae ab illo inventore veritatis et quasi architec to beatae vitae dicta sunt explicabo.</p>
<div class="abs read-more" style="left:121px;top:2664px">Read More</div>
<div class="abs service-photo photo-scissors" role="img" aria-label="Hairdressing scissors arranged on navy fabric"></div>

<div class="abs service-photo photo-garden" role="img" aria-label="Hands working soil with a trowel and hand rake among seedlings"></div>
<h3 class="abs heading service-name" style="left:715px;top:2873px">Garden Tools</h3>
<p class="abs service-text" style="left:715px;top:2936px">Sed ut perspiciatis unde omnis iste natus errorsit voluptatem accusantium doloremque laudantium, totam rem aperiam, eaque ipsa quae ab illo inventore veritatis et quasi archit ecto beatae vitae dicta sulicabo.</p>
<div class="abs read-more" style="left:718px;top:3077px">Read More</div>

<section class="abs quality-banner" role="img" aria-label="Hands honing a large knife on a sharpening stone over a wooden bench">
  <span>Quality Sharpening Service</span>
</section>

<h2 class="abs heading social-handle">@Baybolts</h2>
<div class="abs social-tile tile-1" role="img" aria-label="Knife being honed against a sharpening steel"></div>
<div class="abs social-tile tile-2" role="img" aria-label="Small blue thread snips on a dark surface"></div>
<div class="abs social-tile tile-3" role="img" aria-label="Knife block with knives in a kitchen"></div>
<div class="abs social-tile tile-4" role="img" aria-label="Red pruning shears cutting a branch among leaves"></div>

<footer class="abs site-footer"></footer>
<h4 class="abs footer-heading" style="left:119px">MY ADDRESS</h4>
<svg class="abs" style="left:119px;top:4425px" width="18" height="22" viewBox="0 0 24 30" aria-hidden="true"><path d="M12 0C5.4 0 0 5.2 0 11.7 0 20 12 30 12 30s12-10 12-18.3C24 5.2 18.6 0 12 0zm0 16a4.5 4.5 0 1 1 0-9 4.5 4.5 0 0 1 0 9z" fill="#fff"/></svg>
<p class="abs footer-line" style="top:4426px">18302 Pellman Way, Stevenson<br>Ranch, CA 91381.</p>
<svg class="abs" style="left:119px;top:4480px" width="20" height="20" viewBox="0 0 24 24" aria-hidden="true"><path d="M6.6 10.8a15 15 0 0 0 6.6 6.6l2.2-2.2a1 1 0 0 1 1-.25 11.4 11.4 0 0 0 3.6.57 1 1 0 0 1 1 1V20a1 1 0 0 1-1 1A17 17 0 0 1 3 4a1 1 0 0 1 1-1h3.5a1 1 0 0 1 1 1c0 1.25.2 2.45.57 3.57a1 1 0 0 1-.25 1z" fill="#fff"/></svg>
<p class="abs footer-line" style="top:4481px">Phone: 661-555-0173</p>

<h4 class="abs footer-heading" style="left:518px">CONTACT US</h4>
<div class="abs field" style="left:518px;top:4406px;width:246px;height:34px">Name*</div>
<div class="abs field" style="left:518px;top:4452px;width:246px;height:34px">Email*</div>
<div class="abs field" style="left:518px;top:4498px;width:246px;height:34px">Phone</div>
<div class="abs field" style="left:773px;top:4406px;width:290px;height:126px">Message</div>
<div class="abs submit">SUBMIT</div>
<p class="abs copyright">Copyright 2026 &nbsp;All Rights are Reserved. Privacy Policy</p>

</body>
</html>
```